Business card for new business.
Red and black corporate colors.
Card can have an Indsutrial feel to it. Feel free to add Rust, Bolted steel, or graphics as you see fit. We provide highly specialized services to the below mentioned industries.
Keep information out of corners so that if I want I can choose rounded corners.
Information
- front. name - title - phone - email
- Rear
Refining - Rail - Infrastructure - Mining - Energy
Calgary - Edmonton - Fort McMurray - Revelstoke - Vancouver

```html
<!DOCTYPE html>
<html lang="en">
<head>
<meta charset="utf-8">
<title>Business Card – Front and Back</title>
<link rel="stylesheet" href="https://fonts.googleapis.com/css2?family=Arimo:wght@700&family=Open+Sans:wght@400&display=swap">
<style>
  :root {
    --card-black: #000000;
    --brand-red: #f70000;
    --ink-white: #ffffff;
    --logo-grey: #6b7378;
    --page-bg: #ffffff;
  }
  html, body {
    margin: 0;
    padding: 0;
    width: 1190px;
    height: 1200px;
    overflow: hidden;
    background: var(--page-bg);
  }
  .sheet {
    display: block;
    width: 1190px;
    height: 1200px;
  }
  .card-base { fill: var(--card-black); }
  .red-shape { fill: var(--brand-red); }
  .tab-cutout { fill: var(--card-black); }
  .icon-line { fill: none; stroke: var(--ink-white); stroke-width: 2.5; }
  .icon-fill { fill: var(--ink-white); }
  .icon-red { fill: none; stroke: var(--brand-red); stroke-width: 2.5; }
  .name {
    font-family: "Arimo", Arial, sans-serif;
    font-weight: 700;
    font-size: 70px;
    fill: var(--ink-white);
  }
  .job-title {
    font-family: "Arimo", Arial, sans-serif;
    font-weight: 700;
    font-size: 32px;
    fill: var(--ink-white);
  }
  .contact {
    font-family: "Open Sans", Arial, sans-serif;
    font-weight: 400;
    font-size: 32px;
    fill: var(--ink-white);
  }
  .brand-name {
    font-family: "Arimo", Arial, sans-serif;
    font-weight: 700;
    font-size: 46px;
    letter-spacing: 1px;
    fill: var(--logo-grey);
  }
  .industries {
    font-family: "Open Sans", Arial, sans-serif;
    font-weight: 400;
    font-size: 24px;
    fill: var(--ink-white);
  }
</style>
</head>
<body>
<svg class="sheet" viewBox="0 0 1470 1500" preserveAspectRatio="xMidYMid meet" xmlns="http://www.w3.org/2000/svg">

  <!-- Front of card -->
  <g class="card-front">
    <rect class="card-base" x="203" y="55" width="1064" height="650"/>
    <path class="red-shape header-panel" d="M203 55 H880 L826 313 H203 Z"/>
    <path class="red-shape angle-stripe" d="M203 323 H826 L890 705 H814 L760 357 H203 Z"/>
    <rect class="red-shape edge-tab" x="1239" y="311" width="28" height="136"/>

    <text class="name" x="327" y="193">YOUR NAME</text>
    <text class="job-title" x="335" y="247">CEO / DIRECTOR</text>

    <g class="contact-row phone">
      <path class="red-shape" d="M203 386 H290 L311 407 V460 H203 Z"/>
      <rect class="tab-cutout" x="203" y="403" width="59" height="34"/>
      <path class="icon-fill" d="M272 400 L281 397 L288 411 L282 416 Q285 427 293 434 L299 429 L304 437 L297 446 Q283 444 274 427 Q268 413 272 400 Z"/>
      <text class="contact" x="333" y="433">1.123.123.123.123</text>
    </g>

    <g class="contact-row email">
      <path class="red-shape" d="M203 496 H290 L311 517 V569 H203 Z"/>
      <rect class="tab-cutout" x="203" y="513" width="59" height="34"/>
      <rect class="icon-line" x="267" y="518" width="34" height="23"/>
      <path class="icon-line" d="M267 518 L284 532 L301 518 M267 541 L280 529 M301 541 L288 529"/>
      <text class="contact" x="338" y="539">yourmail@business.com</text>
    </g>

    <g class="contact-row website">
      <path class="red-shape" d="M203 606 H290 L311 627 V678 H203 Z"/>
      <rect class="tab-cutout" x="203" y="623" width="59" height="34"/>
      <circle class="icon-fill" cx="285" cy="641" r="17"/>
      <path class="icon-red" d="M268 641 H302 M285 624 V658 M285 624 Q275 641 285 658 M285 624 Q295 641 285 658"/>
      <text class="contact" x="338" y="649">www.yourwebsite.com</text>
    </g>

    <text class="brand-name" x="1070" y="397" text-anchor="middle">IRONSPAN</text>
  </g>

  <!-- Back of card -->
  <g class="card-back">
    <rect class="card-base" x="202" y="754" width="1065" height="651"/>
    <path class="red-shape diagonal-block" d="M202 754 H600 L430 1405 H202 Z"/>
    <path class="red-shape diagonal-stripe" d="M642 754 H694 L524 1405 H472 Z"/>
    <rect class="red-shape edge-tab" x="1240" y="1011" width="27" height="136"/>

    <text class="brand-name" x="947" y="1097" text-anchor="middle">IRONSPAN</text>
    <text class="industries" x="946" y="1138" text-anchor="middle">Refining, Rail, Infrastructure, Mining, Energy</text>
  </g>

</svg>
</body>
</html>
```